Beacon Stewards Brochure Design*

We host a local leadership development program every two years. We need a brochure to promote the program. We would like it to be 8 1/2 x 11, tri-fold. I have attached a Word document with the necessary info for the brochure. The brochure will be professionally printed. We would like the final design to be in InDesign.

Target Market(s)

Potential participants of our leadership program. They will be local leaders, male and female, from 30-60 years of age.

Requirements
Must have
• Content as detailed in the Word document attached. Our logo.
Nice to have
• A design that is attractive to young professionals.

```html
<!DOCTYPE html>
<html lang="en">
<head>
<meta charset="utf-8">
<title>Beacon Stewards – 2021 Program Brochure</title>
<link rel="stylesheet" href="https://fonts.googleapis.com/css2?family=Raleway:wght@600;700;800&family=Arimo:ital,wght@0,400;0,700;1,400&display=swap">
<style>
  :root{
    --navy:#2b3990; --navy-light:#4a5fb0;
    --blue:#1b9ad7; --blue-light:#3cb3e6;
    --orange:#f26522; --orange-light:#f7941d;
    --green:#0aa64b; --green-light:#3cb64f;
    --gray:#9d9fa2; --gray-light:#b3b5b8;
    --red:#be1e2d;
    --row:#e4e4e5; --bar:#8f9194;
    --ink:#1a1a1a; --accent:#f7941d;
    --rule:#c7c8ca; --page:#ffffff; --stage:#f4f4f4;
  }
  *{box-sizing:border-box;margin:0;padding:0}
  html,body{width:1200px;height:900px;overflow:hidden;background:var(--stage)}
  body{font-family:"Arimo",Arial,sans-serif;color:var(--ink);position:relative}
  .brochure{position:absolute;left:119px;top:78px;width:964px;height:745px;background:var(--page);box-shadow:0 4px 18px rgba(0,0,0,.18);overflow:hidden}
  .abs{position:absolute}

  .overview{left:0;top:0;width:321px;height:224px;background:linear-gradient(160deg,var(--navy) 0%,var(--navy-light) 100%);color:#fff;padding:48px 30px 0 39px}
  .overview h2{font-size:16px;font-weight:700;margin-bottom:13px}
  .overview p{font-size:13.4px;line-height:16px}
  .overview .brand{color:var(--accent);font-weight:700}

  .goal{top:0;height:224px;display:flex;align-items:center;justify-content:center;text-align:center;font-family:"Raleway",sans-serif;font-weight:700;font-size:16.5px;line-height:18.5px;padding:45px 8px 0}
  .goal.blue{left:331px;width:146px;background:linear-gradient(180deg,var(--blue),var(--blue-light));color:var(--ink)}
  .goal.orange{left:487px;width:146px;background:linear-gradient(180deg,var(--orange),var(--orange-light));color:var(--ink)}
  .goal.green{left:643px;width:146px;background:linear-gradient(180deg,var(--green),var(--green-light));color:var(--ink)}
  .goal.gray{left:799px;width:165px;background:linear-gradient(180deg,var(--gray),var(--gray-light));color:var(--ink);padding-right:27px}
  .goal-label{left:396px;top:46px;width:485px;height:22px;background:#fff;font-weight:700;font-size:13px;line-height:22px;text-align:center}

  .fold{top:224px;width:0;height:521px;border-left:1px dotted #555}
  .schedule-rule{left:19px;top:240px;width:926px;height:2px;background:var(--rule)}
  .schedule-title{left:420px;top:233px;width:124px;background:#fff;text-align:center;color:var(--red);font-family:"Raleway",sans-serif;font-weight:700;font-size:12.5px}

  .session{top:255px;width:146px;text-align:center}
  .session .date{background:var(--red);color:#fff;font-family:"Raleway",sans-serif;font-weight:800;font-size:15px;height:22px;line-height:22px}
  .session .topic{height:42px;display:flex;align-items:center;justify-content:center;font-family:"Raleway",sans-serif;font-weight:700;font-size:13.5px;line-height:15px}
  .session .time{background:var(--bar);color:#fff;font-weight:700;font-size:12px;height:18px;line-height:18px;margin-bottom:2px}
  .session ul{list-style:none}
  .session li{font-size:12.2px;line-height:14.5px;padding:2.5px 4px}
  .session li:nth-child(odd){background:var(--row)}
  .session li em{font-style:italic}

  .photo{left:0;top:497px;width:633px;height:248px;background:linear-gradient(180deg,#d9dde3 0%,#8b7d74 55%,#3b3a40 100%)}

  .caption{left:656px;top:499px;width:130px;font-size:10.2px;line-height:12px;font-style:italic}
  .caption strong{font-weight:700}

  .logo{left:656px;top:645px;display:flex;align-items:center;gap:7px;color:var(--navy);font-family:"Raleway",sans-serif;font-weight:800;font-size:15px}
  .logo .dot{width:22px;height:22px;border-radius:50%;background:var(--blue)}

  .graduation{left:799px;top:499px;width:146px;text-align:center}
  .graduation .date{background:var(--red);color:#fff;font-family:"Raleway",sans-serif;font-weight:800;font-size:15px;height:22px;line-height:22px}
  .graduation .topic{font-family:"Raleway",sans-serif;font-weight:700;font-size:13.5px;line-height:15px;padding:6px 0 7px}
  .graduation .time{background:var(--bar);color:#fff;font-weight:700;font-size:12px;height:18px;line-height:18px}
  .graduation p{font-size:12.2px;line-height:15px;padding:3px 2px;background:var(--row)}
  .grad-rule{left:799px;top:672px;width:146px;height:2px;background:#555}

  .contact{right:19px;top:686px;text-align:right;font-size:10.5px;line-height:14px;font-weight:700}
</style>
</head>
<body>
<main class="brochure">
  <section class="overview abs">
    <h2>Program Overview</h2>
    <p><span class="brand">Beacon Stewards</span> is a leadership certification program designed to prepare the leaders of tomorrow. During the five-month program, participants get an in-depth view of community issues, develop leadership skills necessary to assume leadership roles and are exposed to community involvement opportunities.</p>
  </section>

  <div class="goal blue abs">Build and demonstrate leadership and communication skills.</div>
  <div class="goal orange abs">Think critically about key business, policy and civic issues facing Harlow County.</div>
  <div class="goal green abs">Build meaningful, long-lasting connections.</div>
  <div class="goal gray abs">Establish ongoing dialogues with experienced community leaders.</div>
  <div class="goal-label abs">Beacon Stewards will provide participants with the opportunities to:</div>

  <div class="fold abs" style="left:321px"></div>
  <div class="fold abs" style="left:643px"></div>

  <div class="schedule-rule abs"></div>
  <div class="schedule-title abs">2021 SCHEDULE</div>

  <section class="session abs" style="left:19px">
    <div class="date">JANUARY 17</div>
    <div class="topic">Organizational<br>Retreat &amp; Dinner</div>
    <div class="time">10 am - 7 pm</div>
    <ul>
      <li><em>*Attendance Mandatory</em></li>
      <li>Introductions</li>
      <li>Team Building</li>
      <li>Motivation</li>
      <li>Leadership Styles</li>
      <li>Social Hour / Dinner</li>
    </ul>
  </section>

  <section class="session abs" style="left:175px">
    <div class="date">JANUARY 31</div>
    <div class="topic">Business &amp; Industry</div>
    <div class="time">8:30 am - 4 pm</div>
    <ul>
      <li>Business and Industry Panel</li>
      <li>Tour of Ironvale Manufacturing facility</li>
      <li>Tour of Hartwell Tool Company, <em>“Taking your vision into B&amp;I”</em></li>
    </ul>
  </section>

  <section class="session abs" style="left:331px">
    <div class="date">FEBRUARY 21</div>
    <div class="topic">Education</div>
    <div class="time">8:30 am - 4 pm</div>
    <ul>
      <li>Tour of selected programs at RCC</li>
      <li>College Career Program overview</li>
      <li>Lunch at Harlow Career and College Academy</li>
      <li>Tour of HCCA</li>
      <li>Overview of CTE program paths</li>
    </ul>
  </section>

  <section class="session abs" style="left:487px">
    <div class="date">MARCH 14</div>
    <div class="topic">Future Technologies<br>&amp; Communications</div>
    <div class="time">8:30 am - 4 pm</div>
    <ul>
      <li>RCC Presents interview</li>
      <li>Trends and forecasts</li>
      <li>Marketing and communications panel</li>
    </ul>
  </section>

  <section class="session abs" style="left:643px">
    <div class="date">APRIL 4</div>
    <div class="topic">Government</div>
    <div class="time">8:30 am - 4 pm</div>
    <ul>
      <li>Overview of state / federal government</li>
      <li>Overview of city / county government</li>
      <li>Tour of Pine Ridge Correctional Institute</li>
      <li>Tour of courthouse</li>
      <li>Judicial presentations</li>
    </ul>
  </section>

  <section class="session abs" style="left:799px">
    <div class="date">MAY 2</div>
    <div class="topic">Health &amp; Wellness</div>
    <div class="time">8:30 am - 4 pm</div>
    <ul>
      <li>Tour of Riverbend Hospice</li>
      <li>Community Wellness Roundtable</li>
      <li>Tour of Alder Cancer Care Center</li>
      <li>Virtual Medicine Tutorial</li>
      <li>Tour of HRMC</li>
    </ul>
  </section>

  <div class="photo abs" role="img" aria-label="Group photo of program participants standing together"></div>

  <p class="caption abs"><strong>Photo (Left to right):</strong> Sunt quam, quo quodit dolupis,con es remoditi, aut ut que, dem eum consecea, nonsequi dignihi, llaccatus est, ut ligenis, quatisque pore, omnimendit quae, faccum necuptia, vero</p>

  <div class="logo abs"><span class="dot"></span><span>Beacon Stewards</span></div>

  <section class="graduation abs">
    <div class="date">MAY18</div>
    <div class="topic">Graduation Ceremony<br>&amp; Luncheon</div>
    <div class="time">12 pm</div>
    <p>Participants are encouraged to invite their employer/ supervisor/ mentor/ special guest (x2)</p>
  </section>
  <div class="grad-rule abs"></div>

  <address class="contact abs" style="font-style:normal">
    Harlow Chamber of Commerce &amp; Tourism<br>
    214 N. Linden Avenue · Marlowe, North Carolina<br>
    910-555-0148 · www.TheHarlowChamber.com
  </address>
</main>
</body>
</html>
```